Torvale Works- Plumbing Business Card

We need a business card design for a new company that services Canberra and surrounds. We are a professional family-owned plumbing company who has 20+ years' experience. We would like to use our logo as well as the colours black, white, grey and the signature green. The final design needs to communicate professional, high-end, plumbing with reliable service. We provide obligation free quotes and are open 24/7. Services include: Bathroom/kitchen renovations, drainage, stormwater, water leaks, plumbing maintenance, water tanks and septics.

Target Market(s)

Homeowners, real estate agents, builders, small business owners

Industry/Entity Type

Plumbing & Construction

Font styles to use
Serif
Sans Serif

Colors
59FF00
82FF00
B8FF75
E3FFCB
F4FFEA

Requirements
Must have
• Must have logo, example of services and contact details

```html
<!DOCTYPE html>
<html lang="en">
<head>
<meta charset="utf-8">
<title>Torvale Works – Business Card</title>
<link href="https://fonts.googleapis.com/css2?family=Montserrat:wght@400;700;800&family=Roboto:wght@400&family=Roboto+Condensed:wght@700&display=swap" rel="stylesheet">
<style>
  :root {
    --backdrop: #2b2b2b;
    --card: #000000;
    --green: #00a300;
    --white: #ffffff;
    --ink: #0a0a0a;
  }
  * { box-sizing: border-box; margin: 0; padding: 0; }
  html, body { width: 1200px; height: 757px; overflow: hidden; }
  body { background: var(--backdrop); position: relative; font-family: "Montserrat", sans-serif; }

  .card {
    position: absolute; top: 233px; width: 487px; height: 292px;
    background: var(--card); overflow: hidden;
  }
  .card--front { left: 99px; }
  .card--back { left: 615px; }

  .brand-name {
    position: absolute; left: 0; right: 0; text-align: center;
    font-family: "Montserrat", sans-serif; font-weight: 800;
    color: var(--green); letter-spacing: 0.5px; line-height: 1;
  }
  .card--front .brand-name { top: 62px; font-size: 38px; }
  .card--back .brand-name { top: 80px; font-size: 34px; }

  .person-name {
    position: absolute; top: 160px; left: 0; right: 0; text-align: center;
    font-weight: 700; font-size: 22px; color: var(--green); line-height: 1;
  }
  .person-role {
    position: absolute; top: 186px; left: 0; right: 0; text-align: center;
    font-size: 12px; color: var(--white);
  }
  .contact-row {
    position: absolute; top: 211px; left: 0; right: 0;
    display: flex; justify-content: center; gap: 10px;
    font-size: 12px; color: var(--white);
  }
  .contact-item { display: flex; align-items: center; gap: 5px; }
  .contact-icon { width: 15px; height: 15px; display: block; }

  .rule {
    position: absolute; left: 0; right: 0; height: 1px; background: var(--green);
  }
  .card--front .rule { top: 248px; }
  .card--back .rule { top: 194px; }

  .address-pill {
    position: absolute; top: 239px; left: 128px; width: 238px; height: 18px;
    background: var(--green); border-radius: 4px;
    font-size: 11.5px; color: var(--ink); text-align: center; line-height: 18px;
  }

  .services-pill {
    position: absolute; top: 181px; left: 152px; width: 182px; height: 27px;
    background: var(--green); border-radius: 8px;
    font-family: "Roboto Condensed", sans-serif; font-weight: 700;
    font-size: 15.5px; color: var(--white); text-align: center; line-height: 27px;
  }
  .services-list {
    position: absolute; top: 216px; list-style: none;
    font-family: "Roboto", sans-serif; font-size: 12px; color: var(--white);
  }
  .services-list--first { left: 84px; }
  .services-list--second { left: 269px; }
  .services-list li { height: 16.5px; line-height: 16.5px; padding-left: 9px; position: relative; }
  .services-list li::before {
    content: ""; position: absolute; left: 0; top: 7px;
    width: 3px; height: 3px; border-radius: 50%; background: var(--green);
  }
</style>
</head>
<body>
  <section class="card card--front">
    <div class="brand-name">Torvale Works</div>
    <div class="person-name">MARA LINDEN</div>
    <div class="person-role">CEO/Manger</div>
    <div class="contact-row">
      <span class="contact-item">
        <svg class="contact-icon" viewBox="0 0 16 16"><rect width="16" height="16" rx="2" fill="#00a300"/><path d="M5 3.5l2 2.2-1 1.3c.6 1.3 1.6 2.3 2.9 2.9l1.3-1 2.2 2-1 1.8C8 12.7 3.3 8 3.2 4.5z" fill="#fff"/></svg>
        002-555-0148
      </span>
      <span class="contact-item">
        <svg class="contact-icon" viewBox="0 0 16 16"><rect width="16" height="16" rx="2" fill="#00a300"/><rect x="3" y="4.5" width="10" height="7" fill="#fff"/><path d="M3 4.5l5 4 5-4M3 11.5l3.6-3.5M13 11.5L9.4 8" stroke="#00a300" stroke-width="0.9" fill="none"/></svg>
        info@torvaleworks.com
      </span>
      <span class="contact-item">
        <svg class="contact-icon" viewBox="0 0 16 16"><rect width="16" height="16" rx="2" fill="#00a300"/><path d="M5 3v9.5l2.3-2.2 1.6 3.3 1.4-.7-1.6-3.2 3.1-.2z" fill="#fff"/></svg>
        TorvaleWorks.com
      </span>
    </div>
    <div class="rule"></div>
    <div class="address-pill">88 Harlow Ln. Suite 4 Kelmont, TX 0000</div>
  </section>

  <section class="card card--back">
    <div class="brand-name">Torvale Works</div>
    <div class="rule"></div>
    <div class="services-pill">24/7. Services include:</div>
    <ul class="services-list services-list--first">
      <li>Bathroom/kitchen renovations</li>
      <li>Drainage</li>
      <li>Stormwater</li>
    </ul>
    <ul class="services-list services-list--second">
      <li>Water leaks</li>
      <li>Plumbing maintenance</li>
      <li>Water tanks and septics</li>
    </ul>
  </section>
</body>
</html>
```